Ayurvedic Beauty Company in Need of Business Cards

My company is a high-end ayurvedic beauty brand. I need a business card that represents that. The designer should utilize logo and color palette. I want these cards to be printed with the foil accents so keep that in mind.

I have attached the ai of my logo and business card info. As well as, some of the product we are launching soon, they do not have to be on the card.

Be creative and have fun.

Thanks in advance,

Marla

```html
<!DOCTYPE html>
<html lang="en">
<head>
<meta charset="utf-8">
<title>Saffron Bloom Business Card</title>
<link href="https://fonts.googleapis.com/css2?family=Roboto:wght@400;500&family=Roboto+Condensed:wght@700&display=swap" rel="stylesheet">
<style>
  :root {
    --backdrop: #2a2a2a;
    --plum: #761d5a;
    --plum-light: #8e3a73;
    --plum-soft: #843068;
    --gold: #c9a66e;
    --white: #ffffff;
  }
  * { margin: 0; padding: 0; box-sizing: border-box; }
  html, body { width: 1200px; height: 960px; overflow: hidden; }
  body { background: var(--backdrop); position: relative; font-family: "Roboto", Arial, sans-serif; }

  .card { position: absolute; width: 600px; height: 343px; background: var(--plum); overflow: hidden; }
  .card-front { left: 314px; top: 113px; }
  .card-back { left: 311px; top: 472px; }

  /* front */
  .front-bloom { position: absolute; left: 220px; top: 0; width: 380px; height: 343px;
    background:
      radial-gradient(ellipse 62% 58% at 62% 62%, rgba(160, 80, 135, 0.55) 0%, rgba(150, 70, 125, 0.35) 45%, rgba(118, 29, 90, 0) 78%),
      linear-gradient(115deg, rgba(118, 29, 90, 0) 0%, rgba(142, 58, 115, 0.35) 40%, rgba(118, 29, 90, 0.1) 100%); }
  .brand-mark { position: absolute; left: 38px; top: 34px; width: 78px; height: 78px; border-radius: 50%; background: var(--gold); }
  .brand-name { position: absolute; left: 36px; top: 164px; font-weight: 500; font-size: 17px; color: var(--gold); letter-spacing: 0.3px; }

  .contact-list { position: absolute; left: 36px; top: 226px; list-style: none; }
  .contact-list li { display: flex; align-items: center; height: 19.5px; font-size: 15px; color: var(--white); }
  .contact-list li.gap { margin-top: 3px; }
  .contact-list svg { width: 13px; height: 13px; margin-right: 7px; fill: var(--gold); flex: none; }

  .person { position: absolute; left: 368px; top: 250px; width: 200px; text-align: center; }
  .person-name { font-family: "Roboto Condensed", "Arial Narrow", sans-serif; font-weight: 700; font-size: 22px; color: var(--gold); letter-spacing: 0.3px; }
  .person-title { font-size: 15px; font-weight: 500; color: var(--white); margin-top: 1px; }

  /* back */
  .back-pattern { position: absolute; inset: 0;
    background: linear-gradient(180deg, var(--plum-soft) 0%, #7c2360 55%, var(--plum-soft) 100%); }
  .back-brand { position: absolute; left: 47px; top: 244px; font-weight: 500; font-size: 33px; color: var(--gold); letter-spacing: 1px; white-space: nowrap; }
  .back-web { position: absolute; left: 50px; top: 291px; font-size: 14px; color: var(--white); letter-spacing: 4.6px; white-space: nowrap; }
  .product-shot { position: absolute; left: 380px; top: 18px; width: 212px; height: 320px; border-radius: 16px;
    background: linear-gradient(100deg, #e2726a 0%, #f08a7a 38%, #c98a2c 55%, #e9b44a 80%, #b7791f 100%); }
</style>
</head>
<body>

<section class="card card-front" aria-label="Card front">
  <div class="front-bloom" role="img" aria-label="Large faded flower decoration in soft plum tones"></div>
  <div class="brand-mark"></div>
  <div class="brand-name">SAFFRON BLOOM</div>

  <ul class="contact-list">
    <li>
      <svg viewBox="0 0 16 16"><path d="M1 3h14v10H1z"/><path d="M1.5 3.5l6.5 5.5 6.5-5.5" stroke="var(--plum)" stroke-width="1.2" fill="none"/></svg>
      marla@lovesaffronbloom.com
    </li>
    <li>
      <svg viewBox="0 0 16 16"><circle cx="8" cy="8" r="7"/><path d="M1 8h14M8 1c3 3 3 11 0 14M8 1c-3 3-3 11 0 14" stroke="var(--plum)" stroke-width="1" fill="none"/></svg>
      www.lovesaffronbloom.com
    </li>
    <li class="gap">
      <svg viewBox="0 0 16 16"><path d="M3 1l3 3-1.5 2c1 2 3 4 5 5L11.5 9.5l3 3-2 2.5C7 14 2 9 1 3z"/></svg>
      1(888) 555-0148
    </li>
    <li>
      <svg viewBox="0 0 16 16"><rect x="4" y="1" width="8" height="14" rx="1.5"/><rect x="5.3" y="2.8" width="5.4" height="9" fill="var(--plum)"/></svg>
      1(347) 555-0172
    </li>
  </ul>

  <div class="person">
    <div class="person-name">MARLA VENN</div>
    <div class="person-title">CEO</div>
  </div>
</section>

<section class="card card-back" aria-label="Card back">
  <div class="back-pattern" role="img" aria-label="Repeating tone-on-tone floral pattern"></div>
  <div class="back-brand">SAFFRON BLOOM</div>
  <div class="back-web">www.lovesaffronbloom.com</div>
  <div class="product-shot" role="img" aria-label="Two glass dropper bottles: a rose-pink toner and a gold-flecked serum"></div>
</section>

</body>
</html>
```